PSD web site UI

I need a PSD of a web site interface that I can use to build a theme with, which will be used on www.plovix.com, an up-and-coming CMS platform that I developed.

Follow the specifications included within the RAR file download below, and use the included PSD as a reference to make your own unique UI design.

Winners will be chosen based on how clean & professional the design looks, by how many unique panel designs are included within the UI, and by how large of a target market could actually use the design for their business web site.

Contest winners will only need to provide their PSD as completed work.

Download the PSD mockup at the bottom of this page to get started right away!
Updates

Project Deadline Extended
Reason: It was requested that I extend the deadline

Target Market(s)

small businesses and freelance designers, photographers & artists.

Industry/Entity Type

Business

Requirements
Must have
• Your PSD can have any color scheme you want. It can be light, dark, green, blue, multi-colored, paper, metallic, glossy, shiny, solid, gradients, or any theme you can imagine. Be creative, but keep the design looking Web 2.0 & professional. The width of your design can be 960 pixels wide like in the provided mockup PSD, or it can be a 100% width design if you'd like.

-
Panels
-
Each theme requires a minimum of 5 panel designs, which is basically a box that can stretch to a specific width or that stretches to 100% width of the web site. These 5 panels include a header, body, footer, child (that is placed within the body panel), and an alternative body panel. Of course, you can create as many panels as you like to create a more custom theme. Your panels do not have to look like the ones provided in the PSD mockup. They don't have to be completely square with round corners. They could be a bubbly cloud, or wavy, or include garnish around the edges, or be torn paper, or anything you like. Also, you can include a title within some of your panels, which is basically a header design with text at the top of the panel.

Each panel must contain a set of elements that fit the design of the panel. The body of your design should also include this set of elements. These elements include at least one menu, a set of buttons, lorum ipsum text & an anchor link, and form elements, such as a textbox, dropdown, & checkbox.

-
body
-
The body of your design should use a texture, gradient, solid color, or a background image that stretches 100% width. If you separate the body of your design into sectioned rows, each row will be treated like a panel.

-
Dashboard section
-
After a user logs into their account on Plovix.com, they manage their web site via a dashboard. This dashboard has a complex design, but can be partially customized. All elements within the header of the dashboard can be rearranged. This includes the title, screenshot, section title, and section menu. The main menu on the left contains a list of sections within the dashboard, which when clicked, will load the section title & menu in the dashboard header, and load the section page within the body of the dashboard.

Dashboard Icons:
The main menu & other menus within the dashboard contain icons. You can create your own custom icon library to use with your theme if you'd like, and the toolkit comes with a complete set of icons to use if you choose not to create your own library.

Dashboard body:
Each row within the dashboard body (options, search, results, paging) can use a panel design, but the entire dashboard body can also use a panel design as well, so you could design your dashboard body to use just one encompassing panel instead of separate panels for each row if you wanted.

-
Buttons
-
Each panel must contain a set of buttons. Each button requires a regular design as well as a mouse-over design. These types of buttons include: default, apply, cancel, previous, next, and delete (delete should stay small like a "close window" button).

-
Menus
-
Each menu requires a mouse-over design & selected item design.
You can make many types of menus; vertical, horizontal, small, and large.
Each item in the menu can be uniquely designed to create a sequence of menu items. For example, grey, white, grey, white, etc..

-
Photo Gallery
-
each photo container can be uniquely designed, creating a sequence of designs in a list.

-
Comments
-
each comment post can be uniquely designed, creating a sequence of designs in a list.
This will be used for comments as well as twitter feeds.

-
Blog Entries
-
Create designs for a blog summary list & a blog entry details.

Each blog entry (summary or details) can be uniquely designed, creating a sequence of designs in a list.

You could display a title, date created, tag words, summary, and the entry text, but you don't have to display all fields.

-
Product List
-
Products can be displayed many different ways:

product details, list grid, list rows, or even featured products list (with a flashy design).

You can display the product title, price, sale price & sale end date, description, photo & photo gallery, add to cart button, and view product details button. You don't have to display all fields for each design. You could show just a photo & title with summary & no price, or just a photo & title, or just the photo if you wanted.

-
Form elements
-
The textbox can look completely custom, have rounded corners, a textured background, or look plain if you want. The other form elements on the other hand can only be manipulated by CSS, so are very limited in design. Only border color, background color, and text color can be changed. The drop down box can have a custom drop down arrow though.

-
Header Panel
-
Requires a horizontal menu system that can be used for the web site's main menu

-
Footer Panel
-
The footer should be 100% width. Many web sites these days have very creative footers.
Should not have
• Don't use the mockup to just make color changes. I want a completely custom design that uses the structure of the mockup, but has a unique theme to the design, such as paper, dark grungy, cartoonish, hand-drawn, etc. Impress me & impress yourself!

```html
<!DOCTYPE html>
<html lang="en">
<head>
<meta charset="utf-8">
<title>Plovix Dashboard – Blog book</title>
<link rel="stylesheet" href="https://fonts.googleapis.com/css2?family=Open+Sans:wght@300;400;600;700&display=swap">
<style>
:root{
  --page-bg:#d3d3d3;
  --topbar-top:#3a3a3a;
  --topbar-bottom:#151515;
  --panel-dark:#262626;
  --sidebar:#3b3b3b;
  --sidebar-item-top:#4a4a4a;
  --sidebar-item-bottom:#3d3d3d;
  --sidebar-line:#2a2a2a;
  --card:#3c3c3c;
  --card-border:#555;
  --text-light:#e6e6e6;
  --text-muted:#b5b5b5;
  --accent-top:#ff7050;
  --accent-bottom:#e8472a;
  --grey-btn-top:#6a6a6a;
  --grey-btn-bottom:#4c4c4c;
  --field:#f4f4f4;
  --field-text:#a8a8a8;
  --app-green:#3f8b2f;
  --link-accent:#f06a4a;
}
*{box-sizing:border-box;margin:0;padding:0}
html,body{width:1200px;height:849px;overflow:hidden}
body{
  background:repeating-linear-gradient(135deg,#d6d6d6 0 3px,#cecece 3px 6px);
  background-color:var(--page-bg);
  font-family:"Open Sans",Arial,sans-serif;
  color:var(--text-light);
  position:relative;
}
a{color:inherit}

/* Top bar */
.topbar{position:absolute;left:0;top:0;width:1200px;height:53px;background:linear-gradient(var(--topbar-top),var(--topbar-bottom));box-shadow:0 1px 3px rgba(0,0,0,.4)}
.brand{position:absolute;left:157px;top:9px;font-size:33px;font-weight:400;letter-spacing:1px;color:#e8e8e8;line-height:34px}
.main-nav{position:absolute;left:484px;top:0;display:flex;height:53px}
.main-nav a{display:flex;align-items:center;gap:8px;text-decoration:none;font-size:19px;color:#cfcfcf;padding:0 21px;height:53px}
.main-nav a.is-current{background:linear-gradient(#2a2a2a,#1b1b1b);color:#f2f2f2;border-left:1px solid #444;border-right:1px solid #444;padding:0 18px 0 13px}
.main-nav svg{width:18px;height:18px;fill:currentColor}

/* Dashboard shell */
.dashboard{position:absolute;left:150px;top:81px;width:900px;height:800px;background:var(--panel-dark);border-radius:4px 4px 0 0;box-shadow:0 0 6px rgba(0,0,0,.35);overflow:hidden}
.dashboard-head{height:58px;background:linear-gradient(#2d2d2d,#1c1c1c);border-bottom:1px solid #111;position:relative}
.app-mark{position:absolute;left:25px;top:14px;width:22px;height:28px;background:var(--app-green);border-radius:2px}
.dashboard-title{position:absolute;left:65px;top:10px;font-size:28px;font-weight:700;color:#f2f2f2}
.user-menu{position:absolute;right:24px;top:18px;display:flex;align-items:center;gap:10px;font-size:16px;color:#cfcfcf}
.user-menu svg{width:22px;height:22px;fill:#bdbdbd}
.user-menu .caret{font-size:10px;color:#999}

/* Sidebar */
.sidebar{position:absolute;left:0;top:59px;width:164px;bottom:0;background:var(--sidebar);border-right:1px solid #222}
.side-nav{list-style:none}
.side-nav li{height:39.5px;display:flex;align-items:center;padding-left:21px;gap:12px;font-size:13.5px;color:#f0f0f0;background:linear-gradient(var(--sidebar-item-top),var(--sidebar-item-bottom));border-bottom:1px solid var(--sidebar-line);position:relative}
.side-nav .icon{width:18px;height:18px}
.side-nav .go{position:absolute;right:10px;top:11px;width:17px;height:17px;border-radius:50%;background:#2c2c2c;border:1px solid #666;display:flex;align-items:center;justify-content:center}
.side-nav .go svg{width:8px;height:8px;stroke:#ddd;fill:none;stroke-width:2}
.side-nav li.is-active{background:linear-gradient(var(--accent-top),var(--accent-bottom));border-bottom-color:#c23b22;font-size:15px}
.side-nav li.is-active .go{background:none;border:none}
.side-nav li.is-active .app-icon{width:16px;height:20px;background:var(--app-green);border-radius:2px;margin-left:1px}

/* Content */
.content{position:absolute;left:192px;top:0;width:684px;height:800px}
.site-card{position:absolute;top:93px;left:6px;width:600px;height:130px}
.site-shot{position:absolute;left:0;top:0;width:156px;height:116px;border:5px solid #4a4a4a;background:linear-gradient(#2d7fd1 0,#3aa0ee 42%,#f3f5f8 42%,#e8ecf1 100%)}
.site-name{position:absolute;left:187px;top:-4px;font-size:28px;font-weight:300;white-space:nowrap;color:#ececec}
.site-links{position:absolute;left:199px;top:41px;list-style:none;white-space:nowrap}
.site-links li{display:flex;align-items:center;gap:14px;font-size:15px;height:31px}
.site-links svg{width:17px;height:17px;stroke:#9a9a9a;fill:none;stroke-width:1.6}

.panel{position:absolute;left:0;width:684px;background:var(--card);border:1px solid var(--card-border);border-radius:3px;box-shadow:0 1px 2px rgba(0,0,0,.4)}
.folder-panel{top:246px;height:135px}
.folder-row{height:69px;border-bottom:1px solid #2a2a2a;position:relative}
.folder-label{position:absolute;left:43px;top:20px;font-size:20px;font-weight:600;color:#e3e3e3}
.select{position:absolute;left:116px;top:20px;width:536px;height:29px;background:var(--field);border-radius:3px;font-size:15px;color:var(--field-text);padding:3px 12px}
.select::after{content:"";position:absolute;right:11px;top:12px;border:5px solid transparent;border-top:7px solid #999}
.action-row{position:relative;height:64px;border-top:1px solid #4e4e4e}

.btn{position:absolute;height:31px;display:flex;align-items:center;justify-content:center;gap:8px;padding:0 8px;font-size:15px;color:#fff;border-radius:2px;white-space:nowrap}
.btn svg{width:20px;height:20px;flex:none}
.btn-accent{background:linear-gradient(var(--accent-top),var(--accent-bottom));box-shadow:0 1px 2px rgba(0,0,0,.4)}
.btn-grey{background:linear-gradient(var(--grey-btn-top),var(--grey-btn-bottom));box-shadow:0 1px 2px rgba(0,0,0,.4)}
.btn-create{left:21px;top:17px;width:181px}
.btn-all{left:232px;top:17px;width:152px}
.btn-move{left:414px;top:17px;width:263px}

.search-panel{top:403px;height:69px}
.search-field{position:absolute;left:28px;top:20px;width:535px;height:29px;background:var(--field);border-radius:3px;font-size:15px;color:var(--field-text);padding:3px 12px}
.search-field svg{position:absolute;right:9px;top:5px;width:18px;height:18px;stroke:#aaa;fill:none;stroke-width:2}
.btn-search{left:575px;top:20px;width:93px;height:30px;font-size:16.5px}

.entry{height:77px}
.entry-1{top:490px}
.entry-2{top:586px;background:#444}
.check{position:absolute;left:21px;top:17px;width:29px;height:29px;background:#f2f2f2;border-radius:3px;display:flex;align-items:center;justify-content:center}
.check svg{width:18px;height:18px;stroke:#888;fill:none;stroke-width:3}
.entry-title{position:absolute;left:72px;top:8px;font-size:24px;font-weight:300;color:#ececec;white-space:nowrap}
.entry-summary{position:absolute;left:72px;top:45px;font-size:14px;color:var(--text-muted);white-space:nowrap}
.entry-delete{position:absolute;right:12px;top:11px;width:19px;height:19px;border-radius:50%;background:#ccc;display:flex;align-items:center;justify-content:center}
.entry-delete svg{width:9px;height:9px;stroke:#3c3c3c;stroke-width:2.4}

.btn-page{top:676px;width:90px;height:30px;font-size:16.5px}
.btn-prev{left:489px}
.btn-more{left:594px}
.btn-page svg{width:14px;height:14px}

.btn-foot{top:737px;height:31px;font-size:16.5px}
.btn-foot-pages{left:1px;width:100px}
.btn-foot-media{left:123px;width:99px}
.btn-foot-messages{left:244px;width:127px}
.footer-note{position:absolute;left:402px;top:741px;font-size:15px;color:#e2e2e2;white-space:nowrap}
.footer-note a{color:var(--link-accent)}
</style>
</head>
<body>

<header class="topbar">
  <div class="brand">PLOVIX</div>
  <nav class="main-nav">
    <a class="is-current" href="#"><svg viewBox="0 0 20 20"><path d="M2 5h6l2 2h8v10H2z"/></svg>Dashboard</a>
    <a href="#"><svg viewBox="0 0 20 20"><circle cx="10" cy="6" r="4"/><path d="M3 18c0-5 3-7 7-7s7 2 7 7z"/></svg>Community</a>
    <a href="#"><svg viewBox="0 0 20 20"><path d="M13 2l4 4-9 10-5 1 1-5z"/></svg>Developers</a>
    <a href="#"><svg viewBox="0 0 20 20"><path d="M1 4h12v8H6l-3 3v-3H1z"/><path d="M8 14h6l3 3v-3h2V7h-4v6H8z"/></svg>Support</a>
  </nav>
</header>

<main class="dashboard">
  <div class="dashboard-head">
    <span class="app-mark"></span>
    <h1 class="dashboard-title">Blog book</h1>
    <div class="user-menu">
      <svg viewBox="0 0 20 20"><circle cx="10" cy="6" r="4.5"/><path d="M1 19c0-6 4-8 9-8s9 2 9 8z"/></svg>
      Welcome admin <span class="caret">▼</span>
    </div>
  </div>

  <aside class="sidebar">
    <ul class="side-nav">
      <li><svg class="icon" viewBox="0 0 18 18"><rect x="1" y="1" width="16" height="16" fill="#f2f2f2"/><path d="M3 5h12M3 8h12M3 11h12M3 14h12" stroke="#bbb"/></svg>Pages<span class="go"><svg viewBox="0 0 8 8"><path d="M2 1l3 3-3 3"/></svg></span></li>
      <li><svg class="icon" viewBox="0 0 18 18"><rect x="1" y="1" width="16" height="16" fill="#eee"/><rect x="3" y="3" width="12" height="12" fill="#c0642a"/></svg>Media<span class="go"><svg viewBox="0 0 8 8"><path d="M2 1l3 3-3 3"/></svg></span></li>
      <li><svg class="icon" viewBox="0 0 18 18"><rect x="0" y="3" width="18" height="12" fill="#e8e8e8"/><path d="M0 3l9 7 9-7" stroke="#aaa" fill="none"/></svg>Messages<span class="go"><svg viewBox="0 0 8 8"><path d="M2 1l3 3-3 3"/></svg></span></li>
      <li><svg class="icon" viewBox="0 0 18 18"><circle cx="9" cy="9" r="8" fill="#222" stroke="#888"/><circle cx="9" cy="9" r="2" fill="#ddd"/></svg>Analytics<span class="go"><svg viewBox="0 0 8 8"><path d="M2 1l3 3-3 3"/></svg></span></li>
      <li><svg class="icon" viewBox="0 0 18 18"><rect x="1" y="1" width="16" height="16" fill="#f2f2f2"/><path d="M3 5h12M3 8h12M3 11h12M3 14h12" stroke="#bbb"/></svg>Sitemap<span class="go"><svg viewBox="0 0 8 8"><path d="M2 1l3 3-3 3"/></svg></span></li>
      <li><svg class="icon" viewBox="0 0 18 18"><circle cx="9" cy="9" r="6" fill="none" stroke="#ccc" stroke-width="4" stroke-dasharray="3 2"/><circle cx="9" cy="9" r="3.5" fill="#ccc"/></svg>Settings<span class="go"><svg viewBox="0 0 8 8"><path d="M2 1l3 3-3 3"/></svg></span></li>
      <li><svg class="icon" viewBox="0 0 18 18"><rect x="1" y="2" width="16" height="11" fill="#3d7fc9" stroke="#ddd"/><path d="M6 16h6M9 13v3" stroke="#ddd" stroke-width="2"/></svg>Install Apps<span class="go"><svg viewBox="0 0 8 8"><path d="M2 1l3 3-3 3"/></svg></span></li>
      <li class="is-active"><span class="app-icon"></span>Blog book<span class="go"><svg viewBox="0 0 8 8"><path d="M2 1l3 3-3 3"/></svg></span></li>
    </ul>
  </aside>

  <section class="content">
    <div class="site-card">
      <div class="site-shot" role="img" aria-label="Screenshot of the live website home page"></div>
      <h2 class="site-name">Dana Holloway</h2>
      <ul class="site-links">
        <li><svg viewBox="0 0 18 18"><path d="M8 3H2v13h13v-6M11 2h5v5M16 2l-8 8"/></svg><a href="#">View live website</a></li>
        <li><svg viewBox="0 0 18 18"><path d="M8 3H2v13h13v-6M14 2l2 2-8 8H6v-2z"/></svg><a href="#">Edit wensite</a></li>
      </ul>
    </div>

    <div class="panel folder-panel">
      <div class="folder-row">
        <span class="folder-label">Folder</span>
        <div class="select">Select a folder</div>
      </div>
      <div class="action-row">
        <span class="btn btn-accent btn-create"><svg viewBox="0 0 20 20"><path d="M3 1h9l4 4v14H3z" fill="#fff"/><circle cx="14" cy="15" r="4.5" fill="#e8472a" stroke="#fff" stroke-width="1.5"/><path d="M14 12.5v5M11.5 15h5" stroke="#fff" stroke-width="1.5"/></svg>Create New Folder</span>
        <span class="btn btn-grey btn-all"><svg viewBox="0 0 20 20"><path d="M4 1h10l3 3v15H4z" fill="#eee"/><path d="M6 6h8M6 9h8M6 12h8M6 15h5" stroke="#888"/></svg>See all Entries</span>
        <span class="btn btn-grey btn-move"><svg viewBox="0 0 20 20"><path d="M1 4h6l2 2h9v11H1z" fill="#eee"/></svg>Move Selected Entries to Folder</span>
      </div>
    </div>

    <div class="panel search-panel">
      <div class="search-field">Search blog entries<svg viewBox="0 0 18 18"><circle cx="7.5" cy="7.5" r="5.5"/><path d="M11.5 11.5l5 5"/></svg></div>
      <span class="btn btn-accent btn-search">Search</span>
    </div>

    <article class="panel entry entry-1">
      <span class="check"><svg viewBox="0 0 18 18"><path d="M3 9l4 4 8-8"/></svg></span>
      <h3 class="entry-title">A day in the life of Owen Castell.</h3>
      <p class="entry-summary">Explore how Owen Castell spends his time in the Plovix offices.</p>
      <span class="entry-delete"><svg viewBox="0 0 9 9"><path d="M1 1l7 7M8 1L1 8"/></svg></span>
    </article>

    <article class="panel entry entry-2">
      <span class="check"><svg viewBox="0 0 18 18"><path d="M3 9l4 4 8-8"/></svg></span>
      <h3 class="entry-title">It took him 7 years to build Plovix.</h3>
      <p class="entry-summary">Learn about the amazing journey and the struggles Owen had to endure.</p>
      <span class="entry-delete"><svg viewBox="0 0 9 9"><path d="M1 1l7 7M8 1L1 8"/></svg></span>
    </article>

    <nav class="pager">
      <span class="btn btn-accent btn-page btn-prev"><svg viewBox="0 0 20 20"><path d="M10 4L3 10l7 6zM18 4l-7 6 7 6z" fill="#fff"/></svg>Prev</span>
      <span class="btn btn-accent btn-page btn-more">More<svg viewBox="0 0 20 20"><path d="M2 4l7 6-7 6zM10 4l7 6-7 6z" fill="#fff"/></svg></span>
    </nav>

    <div class="footer-row">
      <span class="btn btn-accent btn-foot btn-foot-pages"><svg viewBox="0 0 20 20"><path d="M4 1h9l4 4v14H4z" fill="#fff"/><path d="M7 8h7M7 11h7M7 14h7" stroke="#e8472a"/></svg>Pages</span>
      <span class="btn btn-accent btn-foot btn-foot-media"><svg viewBox="0 0 20 20" fill="#fff"><rect x="2" y="2" width="7" height="7"/><rect x="11" y="2" width="7" height="7"/><rect x="2" y="11" width="7" height="7"/><rect x="11" y="11" width="7" height="7"/></svg>Media</span>
      <span class="btn btn-accent btn-foot btn-foot-messages"><svg viewBox="0 0 20 20"><path d="M1 8l9-6 9 6v10H1z" fill="#fff"/><path d="M1 8l9 6 9-6" stroke="#e8472a" fill="none"/></svg>Messages</span>
      <p class="footer-note">Learn about the amazing <a href="#">Click here</a></p>
    </div>
  </section>
</main>

</body>
</html>
```